Skyscraper Banner 160x600 pixels

Wording -
-----------------------------
Click here for Sydney and NSW events,
places to stay and things to see.

Tavelrimokandu.com.au
-------------------------
Tastefull, in blue and red perhaps , Sydney image/s plenty of white space as that looks good, so not too busy.

The wording is important, the emphasis should be on Accommodation or places to stay while events places to go and things to do come after. This will be placed on www.plorvix.com.au, I like a lot of white space with a clear message.

There's been a lot of designs come in and more to come so please be patient.

```html
<!DOCTYPE html>
<html lang="en">
<head>
<meta charset="utf-8">
<title>plorvix.com.au – Weekend Getaways</title>
<link rel="stylesheet" href="https://fonts.googleapis.com/css2?family=Arimo:wght@400;700&family=Open+Sans:wght@400;600&display=swap">
<style>
:root{
  --page-grey:#dcdcdc;
  --side-grey:#f3f3f3;
  --rule:#cfcfcf;
  --brand-red:#e01b24;
  --link-blue:#0000ee;
  --title-grey:#b9b9b9;
  --label-grey:#9aa0b8;
  --ink:#111;
  --white:#fff;
  --banner-foot:#8c9cab;
  --right-band:#efeced;
}
*{box-sizing:border-box;margin:0;padding:0}
html,body{width:1200px;height:995px;overflow:hidden}
body{background:var(--page-grey);font-family:"Arimo",Arial,sans-serif;color:var(--ink);position:relative}
.abs{position:absolute}
.site{position:absolute;left:62px;top:0;width:1100px;height:995px;background:var(--white);box-shadow:0 0 6px rgba(0,0,0,.25)}
.header-photo{left:0;top:0;width:1100px;height:80px;background:linear-gradient(90deg,#f6f1ee 0%,#f3e6d6 22%,#e3b566 45%,#c98c3b 65%,#8a6a3a 85%,#a07b44 100%)}
.nav-bar{left:0;top:80px;width:1100px;height:30px;background:var(--white);border-top:1px solid #999;border-bottom:1px solid #999}
.site-name{left:6px;top:3px;font-size:21px;color:var(--brand-red);font-weight:400;letter-spacing:-.3px}
.nav-links{right:10px;top:6px;display:flex;gap:18px;font-size:14px}
.nav-links .login{font-weight:700;margin-left:6px}
.tagline-band{left:0;top:110px;width:1100px;height:80px;background:linear-gradient(180deg,#b7a35c 0%,#8e7d3d 45%,#5d4f25 100%)}
.tagline{left:16px;top:53px;font-size:16px;color:var(--white)}
.side-nav{left:0;top:190px;width:182px;height:805px;background:var(--side-grey);border-right:1px dotted var(--rule)}
.side-nav ul{list-style:none;position:absolute;right:0;width:182px}
.side-nav li{height:27.5px;display:flex;justify-content:flex-end;align-items:center;font-size:14px;padding-right:12px}
.side-nav li svg{margin-left:8px}
.main{left:184px;top:190px;width:725px;height:805px}
.page-title{left:16px;top:20px;font-size:22px;font-weight:700;color:var(--title-grey);letter-spacing:1.4px}
.label{font-size:13px;font-weight:700;color:var(--label-grey)}
.search-box{left:9px;top:137px;width:300px;height:24px;border:1px solid #999;background:var(--white)}
.state-map{left:9px;top:182px;width:309px;height:277px;background:radial-gradient(ellipse at 50% 50%,#e27770 0%,#d55e5a 55%,#f4f0f0 75%)}
.mini-brand{left:339px;top:103px;display:flex;align-items:center;gap:6px;font-size:20px;color:var(--brand-red)}
.region-links{left:339px;top:194px;list-style:none}
.region-links li{height:30.3px;font-size:14px;color:var(--link-blue)}
.intro{left:339px;top:451px;width:380px;font-size:14px;line-height:31.5px}
.intro a{color:var(--link-blue);text-decoration:none}
.rule-line{height:1px;background:#555}
.relax{left:14px;top:594px;width:106px;height:153px;background:var(--brand-red)}
.relax span{position:absolute;left:50%;bottom:18px;transform-origin:left bottom;transform:rotate(-90deg) translate(0,50%);font-size:22px;font-weight:700;color:var(--white);letter-spacing:3px;white-space:nowrap}
.feature-photo{left:134px;top:594px;width:204px;height:153px;background:linear-gradient(180deg,#dde6ee 0%,#b9b4a8 45%,#6f7a5a 80%,#8c8a80 100%)}
.feature-text{left:352px;top:594px;width:340px;font-size:13.5px;line-height:16px}
.feature-text a,.listing a{color:var(--link-blue);text-decoration:none}
.listing-photo{top:780px;height:40px}
.listing-bar{top:780px;width:8px;height:30px;background:var(--brand-red)}
.listing{top:778px;width:150px;font-size:14px;line-height:16px}
.right-col{left:909px;top:190px;width:191px;height:805px;background:var(--white)}
.right-band-top{left:0;top:0;width:191px;height:32px;background:var(--right-band)}
.right-band-bottom{left:0;top:775px;width:191px;height:30px;background:var(--right-band)}
.skyscraper{left:1px;top:42px;width:187px;height:702px;background:var(--white);border:1px solid #b9b9b9;overflow:hidden;font-family:"Open Sans",Arial,sans-serif}
.sky-brand{left:0;top:44px;width:187px;text-align:center;font-size:13px;color:var(--brand-red);font-weight:600}
.sky-brand-rule{left:12px;top:64px;width:163px;height:1px;background:var(--brand-red)}
.cta{left:11px;top:71px;width:168px}
.cta-text{position:absolute;left:0;top:10px;width:168px;text-align:center;color:var(--white);font-size:21px;line-height:29px}
.cta-text .big{font-size:26px;line-height:32px}
.offer{left:0;top:272px;width:187px;text-align:center;font-size:21px;line-height:30px;color:var(--ink);z-index:2}
.sky-photo{left:1px;top:318px;width:183px;height:350px;background:linear-gradient(180deg,rgba(255,255,255,0) 0%,#e9ecef 18%,#c9c3b7 45%,#9aa7b3 75%,#7d8d9b 100%)}
.sky-foot{left:0;top:668px;width:187px;height:34px;background:var(--banner-foot);color:var(--white);font-size:14px;padding:9px 0 0 10px}
</style>
</head>
<body>
<div class="site">
  <div class="abs header-photo" role="img" aria-label="Country landscape photo with vineyard and gum trees at sunset"></div>
  <div class="abs nav-bar">
    <div class="abs site-name">plorvix.com.au</div>
    <nav class="abs nav-links"><span>Home</span><span>About Us</span><span>Contact Us</span><span class="login">Login</span></nav>
  </div>
  <div class="abs tagline-band" role="img" aria-label="Vineyard rows photo">
    <div class="abs tagline">The keyword for accommodation, travel, entertainment, holidays and associated services Australia wide.</div>
  </div>

  <aside class="abs side-nav">
    <ul style="top:67px">
      <li>Victoria<svg width="14" height="14"><circle cx="7" cy="7" r="6.5" fill="#ddd"/><circle cx="7" cy="7" r="3" fill="#e01b24"/></svg></li>
      <li>New South Wales<svg width="14" height="14"><circle cx="7" cy="7" r="6.5" fill="#ddd"/><circle cx="7" cy="7" r="3" fill="#e01b24"/></svg></li>
      <li>ACT<svg width="14" height="14"><circle cx="7" cy="7" r="6.5" fill="#ddd"/><circle cx="7" cy="7" r="3" fill="#e01b24"/></svg></li>
      <li>Queensland<svg width="14" height="14"><circle cx="7" cy="7" r="6.5" fill="#ddd"/><circle cx="7" cy="7" r="3" fill="#e01b24"/></svg></li>
      <li>South Australia<svg width="14" height="14"><circle cx="7" cy="7" r="6.5" fill="#ddd"/><circle cx="7" cy="7" r="3" fill="#e01b24"/></svg></li>
      <li>Western Australia<svg width="14" height="14"><circle cx="7" cy="7" r="6.5" fill="#ddd"/><circle cx="7" cy="7" r="3" fill="#e01b24"/></svg></li>
      <li>Northern Territory<svg width="14" height="14"><circle cx="7" cy="7" r="6.5" fill="#ddd"/><circle cx="7" cy="7" r="3" fill="#e01b24"/></svg></li>
      <li>Tasmania<svg width="14" height="14"><circle cx="7" cy="7" r="6.5" fill="#ddd"/><circle cx="7" cy="7" r="3" fill="#e01b24"/></svg></li>
      <li>Norfolk Island<svg width="14" height="14"><circle cx="7" cy="7" r="6.5" fill="#ddd"/><circle cx="7" cy="7" r="3" fill="#e01b24"/></svg></li>
    </ul>
    <ul style="top:385px">
      <li>Advertise with Us<svg width="14" height="14"><circle cx="7" cy="7" r="6.5" fill="#ddd"/><circle cx="7" cy="7" r="3" fill="#e01b24"/></svg></li>
      <li>Testimonials<svg width="14" height="14"><circle cx="7" cy="7" r="6.5" fill="#ddd"/><circle cx="7" cy="7" r="3" fill="#e01b24"/></svg></li>
      <li>Submit a Listing<svg width="14" height="14"><circle cx="7" cy="7" r="6.5" fill="#ddd"/><circle cx="7" cy="7" r="3" fill="#e01b24"/></svg></li>
      <li>Login<svg width="14" height="14"><circle cx="7" cy="7" r="6.5" fill="#ddd"/><circle cx="7" cy="7" r="3" fill="#e01b24"/></svg></li>
    </ul>
  </aside>

  <main class="abs main">
    <h1 class="abs page-title">Weekend Getaways, Holiday Accommodation in Australia</h1>
    <div class="abs label" style="left:10px;top:120px">search by location</div>
    <div class="abs search-box"></div>
    <div class="abs state-map" role="img" aria-label="Map of Australia divided into states, each state clickable"></div>
    <div class="abs label" style="left:10px;top:204px">search by state</div>
    <div class="abs mini-brand"><svg width="16" height="16"><rect width="16" height="16" fill="#e01b24"/></svg>plorvix.com.au</div>
    <ul class="abs region-links">
      <li>Hunter Valley Weekend Accommodation - NSW</li>
      <li>Barossa Weekend Accommodation - South Australia.</li>
      <li>Great Ocean Road Weekend Accommodation - Vic</li>
      <li>Holiday Weekend Accommodation - WA</li>
      <li>Getaway Weekend Accommodation - TAS</li>
      <li>Sunshine Coast Weekend Accommodation - Qld</li>
      <li>Darwin Weekend Accommodation - Northern Territory</li>
      <li>Townsville Weekend Accommodation - Qld</li>
    </ul>
    <p class="abs intro">We publish the phone numbers and web site addresses of the accommodation providers to allow you direct contact.<br>To list your accommodation business <a href="#">Click Here</a></p>

    <div class="abs rule-line" style="left:0;top:578px;width:714px"></div>
    <div class="abs relax"><span>Relax...</span></div>
    <div class="abs feature-photo" role="img" aria-label="Photo of a beachside apartment tower among palm trees"></div>
    <p class="abs feature-text"><a href="#">Vellora on Broadbeach - Broadbeach, QLD.</a><br>Broadbeach Accommodation Best Kept Secret Our small and friendly boutique resort is just 40m from the beach and within easy walking distance of both Broadbeach shops and cafes as well as Surfers Paradise. ...</p>
    <div class="abs rule-line" style="left:0;top:761px;width:714px"></div>

    <div class="abs listing-photo" style="left:17px;width:117px;background:linear-gradient(180deg,#bcd3e6,#c9b79a)" role="img" aria-label="Photo of a country cottage"></div>
    <div class="abs listing-bar" style="left:144px"></div>
    <p class="abs listing" style="left:158px"><a href="#">Ochre Stone Cottage 1 - Daylesford, VIC.</a> A recent</p>
    <div class="abs listing-photo" style="left:374px;width:115px;background:linear-gradient(180deg,#e6e8e2,#8f9a82)" role="img" aria-label="Photo of a holiday house verandah"></div>
    <div class="abs listing-bar" style="left:499px"></div>
    <p class="abs listing" style="left:513px"><a href="#">Pet friendly holiday house - Ocean Grove, VIC.</a> Our</p>
  </main>

  <aside class="abs right-col">
    <div class="abs right-band-top"></div>
    <div class="abs skyscraper">
      <div class="abs sky-brand">Tavelrimokandu.com.au</div>
      <div class="abs sky-brand-rule"></div>
      <div class="abs cta">
        <svg width="168" height="190" viewBox="0 0 168 190"><path d="M10 0H158A10 10 0 0 1 168 10V145A10 10 0 0 1 158 155H80L68 190L56 155H10A10 10 0 0 1 0 145V10A10 10 0 0 1 10 0Z" fill="#e01b24"/></svg>
        <div class="cta-text"><span class="big">CLICK HERE</span><br>FOR SYDNEY<br>AND NSW<br>ATTRACTIONS</div>
      </div>
      <div class="abs sky-photo" role="img" aria-label="Photo of a smiling couple of tourists with a map and camera, pointing up at the sights"></div>
      <div class="abs offer">PLACES TO<br>STAY AND<br>THINGS<br>TO SEE.</div>
      <div class="abs sky-foot">Tavelrimokandu.com.au</div>
    </div>
    <div class="abs right-band-bottom"></div>
  </aside>
</div>
</body>
</html>
```